Medicaid and Nursing Home Planning Law Firm Needs Customizable Flyer

We need a flyer for The Delvecko Law Firm, P.C. that incorporates our logo, color scheme and existing collaterals (see uploads) and that can be easily updated. The flyer could advertise an upcoming speech/seminar/gathering, but the text should be customizable so that we can revise it later on using either MSWord or some other basic software.

Industry/Entity Type

Legal

Requirements
Must have
• Logo and contact information for business, including address, phone number, email and website information
Nice to have
• Also should advertise our 2nd location: 418 Pembury Avenue, Suite 307, Watertown, NY 13607

```html
<!DOCTYPE html>
<html lang="en">
<head>
<meta charset="utf-8">
<title>The Delvecko Law Firm – Flyer</title>
<link rel="stylesheet" href="https://fonts.googleapis.com/css2?family=Questrial&family=Arimo:ital,wght@0,400;0,700;1,700&display=swap">
<style>
  :root {
    --stage: #333231;
    --paper: #ffffff;
    --accent: #f07f1e;
    --ink-grey: #5d5d5d;
    --footer-text: #6a6a6a;
    --white: #ffffff;
    --photo-light: #f3e2c6;
    --photo-sun: #f6a43a;
    --photo-warm: #b4642a;
    --photo-dark: #4a3325;
  }
  * { margin: 0; padding: 0; box-sizing: border-box; }
  html, body {
    width: 1200px; height: 1000px; overflow: hidden;
    background: var(--stage);
  }
  .flyer {
    position: absolute; left: 191px; top: 171px;
    width: 803px; height: 568px;
    background: var(--paper);
    overflow: hidden;
  }
  .hero-photo {
    position: absolute; left: 0; top: 0; width: 803px; height: 435px;
    background:
      radial-gradient(ellipse 260px 150px at 180px 345px, rgba(255,196,90,0.95), rgba(246,164,58,0.55) 45%, rgba(246,164,58,0) 100%),
      linear-gradient(165deg, #ffffff 0%, #fbf4ea 18%, var(--photo-light) 30%, rgba(0,0,0,0) 48%),
      radial-gradient(ellipse 300px 320px at 590px 260px, rgba(60,45,38,0.55), rgba(60,45,38,0) 80%),
      linear-gradient(180deg, #e7c495 0%, var(--photo-warm) 55%, var(--photo-dark) 100%);
  }
  .accent-band {
    position: absolute; left: 0; top: 435px; width: 803px; height: 7px;
    background: var(--accent);
  }
  .brand {
    position: absolute; left: 48px; top: 64px;
    display: flex; align-items: center; gap: 10px;
  }
  .brand-square { width: 14px; height: 14px; background: var(--accent); }
  .brand-name {
    font-family: "Questrial", sans-serif; font-size: 20px;
    color: var(--ink-grey); letter-spacing: 0.5px;
  }
  .headline-rule {
    position: absolute; left: 30px; width: 304px; height: 2px;
    background: var(--white);
  }
  .headline-rule.top { top: 190px; }
  .headline-rule.bottom { top: 332px; }
  .headline {
    position: absolute; left: 38px; top: 196px;
    font-family: "Questrial", sans-serif; font-weight: 400;
    font-size: 30px; line-height: 46px; color: var(--white);
    text-transform: uppercase; letter-spacing: 0;
    white-space: nowrap;
  }
  .practice-areas {
    position: absolute; left: 37px; top: 345px;
    font-family: "Arimo", sans-serif; font-weight: 700;
    font-size: 15.5px; line-height: 19.5px; color: var(--white);
    white-space: nowrap;
  }
  .contact-office, .contact-online {
    position: absolute; top: 462px;
    font-family: "Arimo", sans-serif; font-size: 12.5px; line-height: 21px;
    color: var(--footer-text);
  }
  .contact-office { left: 37px; font-weight: 700; font-style: italic; }
  .contact-online { left: 515px; top: 472px; font-size: 13px; line-height: 20px; }
  .contact-online .web { color: var(--accent); }
  .contact-online .web b { font-weight: 700; }
  .social { display: flex; align-items: center; gap: 8px; }
  .social-square {
    width: 13px; height: 13px; border-radius: 2px; background: var(--accent);
  }
</style>
</head>
<body>
  <main class="flyer">
    <div class="hero-photo" role="img" aria-label="Photo of an older couple embracing, seen from behind, in a field at golden sunset"></div>

    <div class="brand">
      <span class="brand-square"></span>
      <span class="brand-name">THE DELVECKO LAW FIRM</span>
    </div>

    <div class="headline-rule top"></div>
    <h1 class="headline">Protecting<br>everything that<br>matters to you.</h1>
    <div class="headline-rule bottom"></div>

    <p class="practice-areas">New York’s Elder Law, Medicaid,<br>Estate Planning, Trust &amp; Estate<br>Litigation, Guardianship And Special<br>Needs Planning Law Firm</p>

    <div class="accent-band"></div>

    <address class="contact-office">
      418 Pembury Avenue, Suite 307<br>
      Watertown, NY 13607<br>
      Office: (315) 555-0148<br>
      Email: info@thedelveckolawfirm.com
    </address>

    <div class="contact-online">
      <div class="web">www.<b>thedelveckolaw</b>firm.com</div>
      <div class="social"><span class="social-square"></span>linkspace.com/thedelveckolawfirm</div>
      <div class="social"><span class="social-square"></span>chirper: @thedelveckolawfirm</div>
    </div>
  </main>
</body>
</html>
```